A Hair, Beauty and Nails Wholesalers Needs a Business Card Design

We need a business card design for our company which is being passed from parents to daughter, so we wont to re-launch the company with an updated, modern, sophisticated, elegant, chic and fresh look which still incorporates the original colour scheme of Hot Pink, Dark Grey and White. The original logo which is attached can be used on the card but we would like to see some designs with the logo and some without, as we have not yet decided if we want the logo on the card. The name of our company is 'Velmora Supplies' and the name of our website is VelmoraGlowandPolish.example.au. We specialise in supplying a massive range of Hair, Beauty and Nail products to the industry. We are based in QLD, Australia but ship many orders via our website all across Australia.

```html
<!DOCTYPE html>
<html lang="en">
<head>
<meta charset="utf-8">
<title>Velmora Supplies – Business Card</title>
<link href="https://fonts.googleapis.com/css2?family=Lato:wght@300;400;700&display=swap" rel="stylesheet">
<style>
  :root {
    --hot-pink: #e5137f;
    --dark-grey: #7d817e;
    --ink: #0d0d0d;
    --paper: #ffffff;
    --soft-grey: #a9aaa9;
    --light-text: #e6e6e6;
    --backdrop: #d9d9d9;
  }
  * { margin: 0; padding: 0; box-sizing: border-box; }
  html, body {
    width: 1200px; height: 926px; overflow: hidden;
    background: var(--backdrop);
    font-family: "Lato", Arial, sans-serif;
  }
  .canvas {
    position: relative; width: 1200px; height: 926px;
    display: flex; flex-direction: column; align-items: center;
    justify-content: center; gap: 42px;
  }
  .card {
    position: relative; width: 700px; height: 400px; overflow: hidden;
    background: var(--ink);
    box-shadow: 0 6px 18px rgba(0,0,0,.18);
  }
  .card-art { position: absolute; inset: 0; }

  .brand-mark {
    position: absolute; display: flex; align-items: center; gap: 10px;
    color: var(--hot-pink); font-weight: 700; font-size: 34px; letter-spacing: .5px;
    white-space: nowrap;
  }
  .brand-mark .dot {
    width: 18px; height: 18px; border-radius: 50%; background: var(--hot-pink);
  }
  .front .brand-mark { left: 470px; top: 86px; }
  .back .brand-mark { left: 360px; top: 140px; }

  .company-name {
    position: absolute; left: 432px; top: 196px;
    color: var(--hot-pink); font-weight: 700; font-size: 30px; white-space: nowrap;
  }

  .contact-block { position: absolute; left: 56px; top: 150px; }
  .person-name { font-size: 23px; color: var(--soft-grey); font-weight: 300; white-space: nowrap; }
  .person-name strong { font-weight: 700; }
  .person-role { color: var(--hot-pink); font-size: 15px; margin-top: 2px; }
  .contact-list { list-style: none; margin-top: 20px; }
  .contact-list li {
    display: flex; align-items: center; gap: 10px; white-space: nowrap;
    font-size: 15px; font-weight: 300; line-height: 26px; color: var(--light-text);
  }
  .contact-list svg { width: 14px; height: 14px; fill: var(--hot-pink); flex: none; }

  .web-address {
    position: absolute; left: 0; right: 0; top: 270px; text-align: center;
    color: var(--hot-pink); font-size: 15px; letter-spacing: 3.5px; font-weight: 400;
  }
</style>
</head>
<body>
<main class="canvas">

  <section class="card front">
    <svg class="card-art" viewBox="0 0 700 400" width="700" height="400" aria-hidden="true">
      <path fill="var(--paper)" d="M140,0 H700 V350 C600,392 480,380 420,322 C350,255 250,60 140,0 Z"/>
      <path fill="var(--dark-grey)" d="M150,0 C260,58 352,232 425,295 C490,352 600,352 700,300 V316 C600,370 480,370 412,310 C340,246 240,55 140,0 Z"/>
      <path fill="var(--hot-pink)" d="M420,322 C480,380 600,392 700,350 V330 C600,372 490,368 420,322 Z"/>
    </svg>

    <div class="brand-mark"><span class="dot"></span>Velmora</div>
    <div class="company-name">Velmora Supplies</div>

    <div class="contact-block">
      <p class="person-name"><strong>Marisa</strong> Holloway</p>
      <p class="person-role">manager</p>
      <ul class="contact-list">
        <li>
          <svg viewBox="0 0 24 24"><path d="M6.6 10.8a15.1 15.1 0 0 0 6.6 6.6l2.2-2.2a1 1 0 0 1 1-.25 11.4 11.4 0 0 0 3.6.57 1 1 0 0 1 1 1V20a1 1 0 0 1-1 1A17 17 0 0 1 3 4a1 1 0 0 1 1-1h3.5a1 1 0 0 1 1 1c0 1.25.2 2.45.57 3.57a1 1 0 0 1-.25 1z"/></svg>
          (07) 5550 0148
        </li>
        <li>
          <svg viewBox="0 0 24 24"><path d="M2 5h20v14H2z M4 7v.4l8 5.2 8-5.2V7z" fill-rule="evenodd"/></svg>
          admin@velmoraglow.example.au
        </li>
        <li>
          <svg viewBox="0 0 24 24"><path d="M12 2a7 7 0 0 0-7 7c0 5.2 7 13 7 13s7-7.8 7-13a7 7 0 0 0-7-7zm0 9.5A2.5 2.5 0 1 1 12 6.5a2.5 2.5 0 0 1 0 5z"/></svg>
          27 Calloway St, BRINDLEMOOR, NV, 9012
        </li>
      </ul>
    </div>
  </section>

  <section class="card back">
    <svg class="card-art" viewBox="0 0 700 400" width="700" height="400" aria-hidden="true">
      <line x1="0" y1="252" x2="700" y2="252" stroke="var(--hot-pink)" stroke-width="1.5"/>
      <line x1="0" y1="318" x2="700" y2="318" stroke="var(--hot-pink)" stroke-width="1.5"/>
    </svg>
    <div class="brand-mark"><span class="dot"></span>Velmora</div>
    <p class="web-address">WWW.VELMORAGLOWANDPOLISH.EXAMPLE.AU</p>
  </section>

</main>
</body>
</html>
```